Presentation Folder

We are looking for a design for a presentation folder given to clients upon first meeting.

Requirements
Must have
• Corporate contact information on one of the interior sleeves. Must use company logo. Full color interior and exterior. Should have similar feel to business cards and envelopes (see attached samples). If you have trouble with the template files for the folder size, you can visit this site (it is the last option on the page): http://zelvaro.net/g/showStaticPage.do?page=download_templates-pres.html

```html
<!DOCTYPE html>
<html lang="en">
<head>
<meta charset="utf-8">
<title>Alder Ridge Real Estate — Presentation Folder Interior</title>
<link rel="stylesheet" href="https://fonts.googleapis.com/css2?family=Cinzel:wght@400;600&display=swap">
<style>
  :root {
    --backdrop: #ecebea;
    --paper: #f7f7f7;
    --paper-edge: #dcdcdc;
    --maroon: #6e2c32;
    --maroon-dark: #4f1c21;
    --silver-light: #f2f2f2;
    --silver-dark: #9a9a9a;
    --card-text: #f3e9e9;
    --sky: #8fb3d6;
    --foliage: #5d7a4a;
  }
  * { box-sizing: border-box; margin: 0; padding: 0; }
  html, body { width: 1200px; height: 847px; overflow: hidden; background: var(--backdrop); }
  .canvas { position: relative; width: 1200px; height: 847px; }

  .folder { position: absolute; left: 80px; top: 90px; width: 1040px; height: 667px; display: flex; box-shadow: 0 10px 30px rgba(0,0,0,.12); }
  .panel { position: relative; width: 520px; height: 667px; background: var(--paper); }
  .panel--left { border-right: 1px solid var(--paper-edge); }
  .panel--right { overflow: hidden; }

  .pocket { position: absolute; left: 0; top: 0; width: 520px; height: 667px; }

  .business-card { position: absolute; left: 180px; top: 470px; width: 260px; height: 140px; display: flex; background: var(--maroon-dark); box-shadow: 0 2px 6px rgba(0,0,0,.35); font-family: "Cinzel", serif; color: var(--card-text); }
  .card-info { width: 140px; padding: 14px 0 0 12px; display: flex; flex-direction: column; }
  .brand { display: flex; align-items: center; gap: 6px; margin-bottom: 14px; }
  .brand-mark { width: 12px; height: 12px; border-radius: 50%; background: var(--card-text); }
  .brand-name { font-size: 10px; font-weight: 600; line-height: 1.15; }
  .agent-name { font-size: 9px; font-weight: 600; }
  .agent-title { font-size: 6px; margin-bottom: 5px; }
  .contact-line { font-size: 6px; line-height: 1.4; }
  .card-photo { position: relative; flex: 1; background: linear-gradient(180deg, var(--sky) 0%, #c9d9e6 50%, var(--foliage) 100%); }
  .badges { position: absolute; left: -34px; bottom: 12px; display: flex; gap: 4px; }
  .badge { width: 9px; height: 9px; background: var(--card-text); }
</style>
</head>
<body>
<main class="canvas">
  <div class="folder">
    <section class="panel panel--left" aria-label="Left interior panel"></section>
    <section class="panel panel--right" aria-label="Right interior panel with pocket">
      <svg class="pocket" viewBox="0 0 520 667" aria-hidden="true">
        <defs>
          <linearGradient id="pocketFill" x1="0" y1="0" x2="1" y2="0">
            <stop offset="0" stop-color="var(--maroon-dark)"/>
            <stop offset="1" stop-color="var(--maroon)"/>
          </linearGradient>
          <linearGradient id="silverEdge" x1="0" y1="0" x2="1" y2="0">
            <stop offset="0" stop-color="var(--silver-dark)"/>
            <stop offset=".5" stop-color="var(--silver-light)"/>
            <stop offset="1" stop-color="var(--silver-dark)"/>
          </linearGradient>
        </defs>
        <path d="M120 420 Q40 500 22 667 L520 667 L520 420 Z" fill="url(#pocketFill)"/>
        <path d="M120 420 Q40 500 22 667" fill="none" stroke="url(#silverEdge)" stroke-width="10"/>
        <path d="M178 468 L442 468" stroke="var(--maroon-dark)" stroke-width="2" opacity=".6"/>
      </svg>

      <article class="business-card">
        <div class="card-info">
          <div class="brand">
            <span class="brand-mark"></span>
            <span class="brand-name">Alder Ridge<br>Real Estate</span>
          </div>
          <p class="agent-name">Martin Halvey</p>
          <p class="agent-title">Principal Broker &amp; Owner</p>
          <p class="contact-line">Martin@AlderRidgeHomes.com</p>
          <p class="contact-line">(410) 555-0172 Mobile</p>
          <p class="contact-line">(443) 555-0148 Office</p>
          <p class="contact-line">(443) 555-0193 Fax</p>
        </div>
        <div class="card-photo" role="img" aria-label="Portrait photo of the broker in front of a house">
          <div class="badges"><span class="badge"></span><span class="badge"></span></div>
        </div>
      </article>
    </section>
  </div>
</main>
</body>
</html>
```